Professional Modern Website Design

We are a premium IT services provider to the financial industry based in London. Our company is called Veltra our current holding page is www.veltra-example.co.uk. We require a new website to match our new corporate identity. This project is for the design phase only. Development will be handled in-house. I have attached examples of wire frames we have developed (although open to suggestions for improvement) Our brand document that should demonstrate current brand, inc how we communicate to potential clients and finally mostly completed web-content.
We are looking for designers that can create something that sets us apart from our competitors.
Target Market(s)
IT Decision makers in Finance companies such as; hedge funds, private investment banks etc
Industry/Entity Type
Financial
Number of Pages Required
5+ page
Requirements
Must have
- hexagon elements in the design, unique design.
Nice to have
- Blog and social media feeds
Should not have
- Should not resemble a downloaded template

```html
<!DOCTYPE html>
<html lang="en">
<head>
<meta charset="utf-8">
<title>Veltra – Data Centre &amp; Infrastructure</title>
<link href="https://fonts.googleapis.com/css2?family=Dosis:wght@400;500;600;700&family=Open+Sans:wght@400;600;700&display=swap" rel="stylesheet">
<style>
:root{
  --orange:#f4861f;
  --orange-deep:#e8761a;
  --ink:#222222;
  --text:#444444;
  --muted:#666666;
  --line:#e3e3e3;
  --hero-dark:#2f3234;
  --footer:#0d0d0d;
  --white:#ffffff;
  --gold:#f5b81c;
  --map:#ece6d8;
}
*{box-sizing:border-box;margin:0;padding:0}
html,body{width:1200px;height:2380px;overflow:hidden;background:var(--white)}
body{position:relative;font-family:"Open Sans",Arial,sans-serif;color:var(--text)}
.abs{position:absolute}
svg.layer{position:absolute;left:0;top:0}

/* header */
.site-header{position:absolute;left:0;top:0;width:1200px;height:80px;background:var(--white);border-top:3px solid var(--orange);z-index:5}
.brand{position:absolute;left:150px;top:6px;width:70px;text-align:center}
.brand-mark{display:block;width:40px;height:40px;margin:0 auto;background:var(--orange)}
.brand-name{display:block;font-family:"Dosis",sans-serif;font-size:11px;letter-spacing:2px;color:var(--muted);margin-top:4px}
.main-nav{position:absolute;left:496px;top:0;display:flex;font-family:"Dosis",sans-serif;font-size:14px;font-weight:500;text-transform:uppercase;color:var(--ink)}
.main-nav a{color:inherit;text-decoration:none;display:block;height:80px;line-height:80px;padding:0 22px}
.main-nav a.active{background:var(--orange);color:var(--white);width:76px;padding:0;text-align:center;height:82px;clip-path:polygon(0 0,100% 0,100% 88%,50% 100%,0 88%)}

/* hero */
.hero{position:absolute;left:0;top:80px;width:1200px;height:482px;clip-path:polygon(0 0,100% 0,100% 92%,53.3% 93%,50% 100%,46.7% 93%,0 95%);background:linear-gradient(180deg,#3a3d3f 0%,#2b2e30 55%,#3b3e40 100%)}
.hero-photo{position:absolute;right:0;top:0;width:400px;height:100%;background:linear-gradient(100deg,rgba(60,62,64,0) 0%,#8a8f90 18%,#c9c2b3 45%,#dcd6c8 70%,#9aa3a8 100%)}
.hero-copy{position:absolute;left:158px;top:110px;width:450px;color:#e8e8e8}
.hero-title{font-family:"Dosis",sans-serif;font-weight:700;font-size:32px;color:var(--gold);margin-bottom:20px}
.hero-copy p{font-size:11.6px;line-height:18px;margin-bottom:4px}
.btn-more{position:absolute;left:158px;top:352px;width:132px;height:34px;background:var(--orange);color:var(--white);font-family:"Dosis",sans-serif;font-weight:700;font-size:13px;text-align:center;line-height:34px;clip-path:polygon(12% 0,88% 0,100% 50%,88% 100%,12% 100%,0 50%)}

/* intro */
.section-title{position:absolute;left:0;width:1200px;text-align:center;font-family:"Dosis",sans-serif;font-weight:400;font-size:40px;color:var(--ink);letter-spacing:1px}
.intro-sub{position:absolute;left:0;top:636px;width:1200px;text-align:center;font-family:"Dosis",sans-serif;font-weight:600;font-size:14px;color:var(--ink);text-transform:uppercase}
.service{position:absolute;top:696px;width:300px;text-align:center}
.service svg{display:block;margin:0 auto}
.service h3{font-family:"Dosis",sans-serif;font-weight:700;font-size:24px;color:var(--ink);margin:18px 0 10px;text-transform:uppercase}
.service p{font-size:12px;line-height:19px;color:var(--text);padding:0 20px}

/* testimonials */
.testimonial-band{position:absolute;left:0;top:1150px;width:1200px;height:380px}
.testimonial-quote{position:absolute;left:190px;top:1326px;width:820px;text-align:center;color:var(--white);font-size:13px;line-height:22px}
.quote-mark{position:absolute;left:0;top:1286px;width:1200px;text-align:center;color:var(--white);font-family:Georgia,serif;font-size:42px;line-height:30px;font-weight:700}
.author{position:absolute;left:640px;top:1418px;color:var(--white);font-family:"Dosis",sans-serif;font-weight:600;font-size:13px;text-transform:uppercase;font-style:normal}

/* partners */
.partner-grid{position:absolute;left:162px;top:1640px;width:878px;display:grid;grid-template-columns:repeat(4,202px);grid-template-rows:72px 72px;column-gap:23px;row-gap:22px}
.partner{border:1px solid var(--line);display:flex;align-items:center;justify-content:center;font-family:"Open Sans",sans-serif;font-weight:700;font-size:22px}

/* map + office */
.office{position:absolute;left:770px;top:1905px;width:270px;height:340px;color:var(--white);text-align:center}
.office h4{position:absolute;left:0;top:92px;width:270px;font-family:"Dosis",sans-serif;font-weight:700;font-size:18px}
.office ul{position:absolute;left:30px;top:130px;width:220px;list-style:none;font-size:11px;line-height:17px}
.office li{display:flex;gap:8px;align-items:flex-start;margin-bottom:14px;text-align:center}
.office li span{flex:1}

/* footer */
.social{position:absolute;left:540px;top:2318px;display:flex;gap:14px}
.social i{display:block;width:30px;height:30px;background:var(--white);border-radius:50%}
.copyright{position:absolute;left:0;top:2354px;width:1200px;text-align:center;color:#cfcfcf;font-size:11px}
</style>
</head>
<body>

<header class="site-header">
  <a class="brand" href="#"><span class="brand-mark"></span><span class="brand-name">VELTRA</span></a>
  <nav class="main-nav">
    <a class="active" href="#">Home</a>
    <a href="#">About</a>
    <a href="#">Services</a>
    <a href="#">Partners</a>
    <a href="#">Clients</a>
    <a href="#">Contact</a>
  </nav>
</header>

<section class="hero" role="img" aria-label="City skyline with a tall glass office tower at dusk">
  <div class="hero-photo"></div>
  <div class="hero-copy">
    <h1 class="hero-title">Data Centre &amp; Infrastructure</h1>
    <p>We set our standards high, aiming to become an industry leader within the finance sector for delivering secure, scalable and always available infrastructure.</p>
    <p>We consult with you on data centre best practices. We will consider the data centre location, provider and design, including build and configuration to make sure it aligns with your expectations.</p>
    <p>We merge the best products with top-class maintenance services to ensure our integration meets your objectives.</p>
  </div>
  <a class="btn-more" href="#">READ MORE</a>
</section>

<h2 class="section-title" style="top:580px">VELTRA</h2>
<p class="intro-sub">Veltra is one of the leading systems integrators to the world's finance sector.</p>

<article class="service" style="left:126px">
  <svg width="182" height="206" viewBox="0 0 182 206">
    <polygon points="91,3 179,53 179,153 91,203 3,153 3,53" fill="#ffffff" stroke="#555" stroke-width="5"/>
    <defs><linearGradient id="g1" x1="0" y1="0" x2="1" y2="1"><stop offset="0" stop-color="#cfd2d4"/><stop offset="1" stop-color="#8c9194"/></linearGradient></defs>
    <polygon role="img" aria-label="Business analysis chart under a magnifying glass" points="91,14 169,59 169,147 91,192 13,147 13,59" fill="url(#g1)"/>
  </svg>
  <h3>Analysis &amp; Assessment</h3>
  <p>We will analyse your current infrastructure and assess what you need to help your business grow. We can offer advice on both on and off-premise solutions to meet compliance and your enterprise's objectives.</p>
</article>

<article class="service" style="left:444px">
  <svg width="182" height="206" viewBox="0 0 182 206">
    <polygon points="91,3 179,53 179,153 91,203 3,153 3,53" fill="#ffffff" stroke="#555" stroke-width="5"/>
    <defs><linearGradient id="g2" x1="0" y1="0" x2="1" y2="1"><stop offset="0" stop-color="#e9c9b3"/><stop offset="0.5" stop-color="#f1e4d8"/><stop offset="1" stop-color="#c9a58f"/></linearGradient></defs>
    <polygon role="img" aria-label="Hands joining jigsaw puzzle pieces" points="91,14 169,59 169,147 91,192 13,147 13,59" fill="url(#g2)"/>
  </svg>
  <h3>Implementation</h3>
  <p>We will implement the best solutions for you and ensure everything you need is set up without a gap in service. If you need to migrate applications or services, we will ensure it runs smoothly and all risks are addressed ahead of time.</p>
</article>

<article class="service" style="left:750px">
  <svg width="182" height="206" viewBox="0 0 182 206">
    <polygon points="91,3 179,53 179,153 91,203 3,153 3,53" fill="#ffffff" stroke="#555" stroke-width="5"/>
    <defs><linearGradient id="g3" x1="0" y1="0" x2="0" y2="1"><stop offset="0" stop-color="#8fcbe9"/><stop offset="0.55" stop-color="#4fb04a"/><stop offset="1" stop-color="#3c8f3a"/></linearGradient></defs>
    <polygon role="img" aria-label="Green currency symbol surrounded by scaffolding against a blue sky" points="91,14 169,59 169,147 91,192 13,147 13,59" fill="url(#g3)"/>
  </svg>
  <h3>Adapt &amp; Grow</h3>
  <p>Although everything we do is scalable, we understand businesses change. We will continually assess your needs and adapt as you do. Because we are an integrator, we can watch from the sidelines to ensure opportunities are never missed.</p>
</article>

<svg class="layer" width="1200" height="2380" style="pointer-events:none">
  <polygon points="0,1175 560,1172 600,1156 640,1172 1200,1165 1200,1505 640,1500 600,1523 560,1500 0,1512" fill="var(--orange)"/>
  <polyline points="112,1335 100,1365 112,1395" fill="none" stroke="#fbd3ac" stroke-width="3"/>
  <polyline points="1088,1335 1100,1365 1088,1395" fill="none" stroke="#fbd3ac" stroke-width="3"/>
</svg>

<h2 class="section-title" style="top:1216px;color:var(--white)">TESTIMONIALS</h2>
<div class="quote-mark">&ldquo;</div>
<p class="testimonial-quote">With so many products and services running in the cloud, it can be a headache for IT managers to keep track. Veltra will help you discover the agility and cost savings associated with cloud-based applications without the burden of managing them in-house.</p>
<svg class="abs" style="left:566px;top:1388px" width="64" height="72" viewBox="0 0 64 72">
  <polygon points="32,2 62,19 62,53 32,70 2,53 2,19" fill="#ffffff"/>
  <polygon role="img" aria-label="Portrait of the quoted client" points="32,8 57,22 57,50 32,64 7,50 7,22" fill="#9aa0a6"/>
</svg>
<cite class="author">- Lin Haoren</cite>

<h2 class="section-title" style="top:1560px">OUR PARTNER</h2>
<div class="partner-grid">
  <div class="partner" style="color:#5a9e3a">Brightstack</div>
  <div class="partner" style="color:#1b4f8f">Harlow Kent</div>
  <div class="partner" style="color:#555555">Northgate</div>
  <div class="partner" style="color:#1d3e8a">Lenmark</div>
  <div class="partner" style="color:#222222">Puffin Works</div>
  <div class="partner" style="color:#333333">Cloudmere</div>
  <div class="partner" style="color:#111111">Vectorline</div>
  <div class="partner" style="color:#1f9bbf">Ferrox</div>
</div>

<svg class="layer" width="1200" height="2380" style="top:0">
  <polygon role="img" aria-label="Street map of central London around Mayfair" points="0,1882 1200,1860 1200,2262 0,2262" fill="var(--map)"/>
  <polygon points="0,2270 1200,2248 1200,2380 0,2380" fill="var(--footer)"/>
  <polygon points="770,1932 905,1905 1040,1932 1040,2242 770,2242" fill="var(--orange)"/>
  <polygon points="905,1918 938,1937 938,1975 905,1994 872,1975 872,1937" fill="#ffffff"/>
  <rect x="893" y="1944" width="24" height="24" fill="var(--orange)"/>
</svg>

<section class="office">
  <h4>OUR OFFICE</h4>
  <ul>
    <li><svg width="10" height="14" viewBox="0 0 10 14"><path d="M5 0a5 5 0 0 1 5 5c0 4-5 9-5 9S0 9 0 5a5 5 0 0 1 5-5z" fill="#fff"/></svg><span>12 Larkspur Yard, Orchard Lane, Southend, Essex SS0 0AA</span></li>
    <li><svg width="10" height="14" viewBox="0 0 10 14"><path d="M5 0a5 5 0 0 1 5 5c0 4-5 9-5 9S0 9 0 5a5 5 0 0 1 5-5z" fill="#fff"/></svg><span>40 Example Street, Mayfair, London, W1A 0XX</span></li>
    <li><svg width="12" height="12" viewBox="0 0 12 12"><path d="M2 0l3 3-1.5 2a7 7 0 0 0 3.5 3.5L9 7l3 3-2 2C5 12 0 7 0 2z" fill="#fff"/></svg><span>+44 20 0000 1234 - 35</span></li>
    <li><svg width="13" height="10" viewBox="0 0 13 10"><rect width="13" height="10" fill="#fff"/><polyline points="0,0 6.5,5 13,0" fill="none" stroke="#f4861f" stroke-width="1.2"/></svg><span>info@veltra-example.co.uk</span></li>
  </ul>
</section>

<footer>
  <div class="social"><i></i><i></i><i></i></div>
  <p class="copyright">Copyright &copy; 2014 Veltra Limited - All Rights Reserved</p>
</footer>

</body>
</html>
```